Stationery for Public Accountant Practice

Name of Practice
Holloway Merrick Pty Ltd
Tel: 0413927056
Postal Address : PO Box 482, Oakvale East, Vic 3187

Target Market(s)

Small Business Clients

Industry/Entity Type

Accounting

Font styles to use
Serif

Requirements
Must have
• Letterhead, business card, With compliments slip
Nice to have
• Conservative

```html
<!DOCTYPE html>
<html lang="en">
<head>
<meta charset="utf-8">
<title>Holloway Merrick Pty Ltd — Stationery</title>
<link href="https://fonts.googleapis.com/css2?family=EB+Garamond:ital,wght@0,400;0,600;1,500&display=swap" rel="stylesheet">
<style>
  :root {
    --backdrop: #ecebe8;
    --paper: #ffffff;
    --sky: #cfe4f6;
    --stripe: #139fdc;
    --navy: #1474bd;
    --azure: #25a8e0;
    --slate: #a7a9ae;
    --ink: #1a6db5;
    --on-dark: #ffffff;
  }
  * { margin: 0; padding: 0; box-sizing: border-box; }
  html, body { width: 1200px; height: 1200px; overflow: hidden; }
  body {
    background: var(--backdrop);
    position: relative;
    font-family: "EB Garamond", Georgia, serif;
  }
  .sheet {
    position: absolute;
    background: var(--paper);
    overflow: hidden;
    box-shadow: 0 2px 6px rgba(0,0,0,0.12);
  }
  .sheet-art { position: absolute; inset: 0; width: 100%; height: 100%; }
  .sky { fill: var(--sky); }
  .stripe { fill: var(--stripe); }
  .navy { fill: var(--navy); }
  .azure { fill: var(--azure); }
  .slate { fill: var(--slate); }

  .practice-name {
    position: absolute;
    color: var(--ink);
    font-weight: 600;
    white-space: nowrap;
  }
  .contact-line {
    position: absolute;
    display: flex;
    align-items: center;
    color: var(--on-dark);
    white-space: nowrap;
  }
  .contact-item { display: flex; align-items: center; }
  .icon { flex: none; }
  .icon-bg { fill: var(--azure); }
  .icon-glyph { fill: var(--navy); }

  /* Letterhead */
  .letterhead { left: 40px; top: 240px; width: 555px; height: 718px; }
  .letterhead .practice-name { left: 33px; top: 24px; font-size: 29px; }
  .letterhead .contact-line { left: 27px; top: 678px; font-size: 11.5px; gap: 7px; }
  .letterhead .contact-item { gap: 4px; }
  .letterhead .icon { width: 17px; height: 17px; }

  /* Compliments slip */
  .comp-slip { left: 620px; top: 381px; width: 540px; height: 254px; }
  .comp-slip .practice-name { left: 16px; top: 13px; font-size: 15px; }
  .comp-slip .greeting {
    position: absolute; right: 16px; top: 40px;
    color: var(--ink); font-style: italic; font-weight: 500; font-size: 11px;
  }
  .comp-slip .contact-line { left: 16px; top: 220px; font-size: 7.8px; gap: 4px; }
  .comp-slip .contact-item { gap: 3px; }
  .comp-slip .icon { width: 11px; height: 11px; }

  /* Business card */
  .business-card { left: 776px; top: 689px; width: 228px; height: 130px; }
  .business-card .practice-name { left: 28px; top: 46px; font-size: 14px; }
  .business-card .card-contacts {
    position: absolute; left: 8px; top: 91px;
    color: var(--on-dark); font-size: 6.3px; line-height: 1.3;
  }
  .business-card .card-row { display: flex; align-items: flex-start; gap: 3px; margin-bottom: 4px; }
  .business-card .icon { width: 7px; height: 7px; margin-top: 0.5px; }
</style>
</head>
<body>

<svg width="0" height="0" style="position:absolute" aria-hidden="true">
  <defs>
    <symbol id="icon-phone" viewBox="0 0 20 20">
      <rect class="icon-bg" width="20" height="20" rx="3"/>
      <path class="icon-glyph" d="M6.2 3.5c.5-.3 1.1-.2 1.4.3l1.3 2.2c.3.5.2 1-.2 1.4l-.9.8c.7 1.5 1.9 2.7 3.4 3.4l.8-.9c.4-.4 1-.5 1.4-.2l2.2 1.3c.5.3.6.9.3 1.4l-.8 1.2c-.4.6-1.1.9-1.8.8C8.4 14.6 5.4 11.6 4.8 6.7c-.1-.7.2-1.4.8-1.8z"/>
    </symbol>
    <symbol id="icon-pin" viewBox="0 0 20 20">
      <rect class="icon-bg" width="20" height="20" rx="3"/>
      <path class="icon-glyph" d="M10 3.2a4.6 4.6 0 0 0-4.6 4.6c0 3.4 4.6 8.8 4.6 8.8s4.6-5.4 4.6-8.8A4.6 4.6 0 0 0 10 3.2zm0 6.5a1.9 1.9 0 1 1 0-3.8 1.9 1.9 0 0 1 0 3.8z"/>
    </symbol>
  </defs>
</svg>

<section class="sheet letterhead" aria-label="Letterhead">
  <svg class="sheet-art" viewBox="0 0 694 898" preserveAspectRatio="none" aria-hidden="true">
    <polygon class="sky" points="0,0 694,0 694,63 0,122"/>
    <polygon class="stripe" points="0,122 694,63 0,146"/>
    <polygon class="sky" points="0,146 694,63 0,166"/>
    <polygon class="navy" points="0,770 450,852 694,898 0,898"/>
    <polygon class="slate" points="450,852 694,782 694,802"/>
    <polygon class="azure" points="450,852 694,802 694,898"/>
  </svg>
  <h1 class="practice-name">Holloway Merrick Pty Ltd</h1>
  <div class="contact-line">
    <span class="contact-item"><svg class="icon"><use href="#icon-phone"/></svg>04 1392 7056</span>
    <span class="contact-item"><svg class="icon"><use href="#icon-pin"/></svg>PO Box 482, Oakvale East, Vic 3187</span>
  </div>
</section>

<section class="sheet comp-slip" aria-label="With compliments slip">
  <svg class="sheet-art" viewBox="0 0 675 318" preserveAspectRatio="none" aria-hidden="true">
    <polygon class="sky" points="0,0 675,0 675,12 0,70"/>
    <polygon class="stripe" points="0,70 675,12 0,82"/>
    <polygon class="sky" points="0,82 675,12 0,92"/>
    <polygon class="navy" points="0,224 450,286 675,318 0,318"/>
    <polygon class="slate" points="450,286 675,236 675,256"/>
    <polygon class="azure" points="450,286 675,256 675,318"/>
  </svg>
  <h2 class="practice-name">Holloway Merrick Pty Ltd</h2>
  <p class="greeting">With compliments</p>
  <div class="contact-line">
    <span class="contact-item"><svg class="icon"><use href="#icon-phone"/></svg>04 1392 7056</span>
    <span class="contact-item"><svg class="icon"><use href="#icon-pin"/></svg>PO Box 482, Oakvale East, Vic 3187</span>
  </div>
</section>

<section class="sheet business-card" aria-label="Business card">
  <svg class="sheet-art" viewBox="0 0 285 162" preserveAspectRatio="none" aria-hidden="true">
    <polygon class="sky" points="0,0 285,0 285,6 0,28"/>
    <polygon class="stripe" points="0,28 285,6 0,38"/>
    <polygon class="sky" points="0,38 285,6 0,46"/>
    <polygon class="navy" points="0,90 182,135 285,162 0,162"/>
    <polygon class="slate" points="182,135 285,94 285,102"/>
    <polygon class="azure" points="182,135 285,102 285,162"/>
  </svg>
  <h2 class="practice-name">Holloway Merrick Pty Ltd</h2>
  <div class="card-contacts">
    <div class="card-row"><svg class="icon"><use href="#icon-phone"/></svg><span>04 1392 7056</span></div>
    <div class="card-row"><svg class="icon"><use href="#icon-pin"/></svg><span>PO Box 482<br>Oakvale East, Vic 3187</span></div>
  </div>
</section>

</body>
</html>
```